Non Profit Company Looking For New Website

The website for Corvale Paddock Rehoming Society should offer the viewer beautiful photos that inspire condifence and joy and tap into our love of horses.

We would like to see a website that displays trust, quality and confidence. Needs to be responsive and mobile friendly for all browsers and coded for both Android & IOS.

READ ATTACHED WEBSITE TEMPLATE FOR COMPLETE DETAILS ON WHAT WE ARE LOOKING FOR.

Looking for recommmendations if we should use WordPress/WooCommerce for site or Wordpress with Shopify Plug in or just Shopify.

Must be both desktop and mobile friendly with fast page load speed. Need the ability to edit ourselves.

Industry/Entity Type

Non Profit

Coding

Coded - Design and coding required

Number of Pages Required

5+ page

Requirements
Must have
• We would like to see a website that displays trust, quality and confidence. Needs to be responsive and mobile friendly for all browsers and coded for both Android & IOS.

Looking for recommendations if we should use WordPress/WooCommerce for site or Wordpress with Shopify Plug in or just Shopify.

Logo Colour:
Pantone 7621 C

READ TEMPLATE THAT IS ATTACHED
Nice to have
• Like look of this website as a sample:
https://www.quillmanegallop.com/

Another similar non profit organization
https://brindlefieldrest.com/

```html
<!DOCTYPE html>
<html lang="en">
<head>
<meta charset="utf-8">
<title>Corvale Paddock Rehoming Society</title>
<link href="https://fonts.googleapis.com/css2?family=Tinos:wght@400;700&family=Open+Sans:wght@400;600&display=swap" rel="stylesheet">
<style>
:root{
  --red:#b00a22;
  --pink:#f1d3d8;
  --ink:#333;
  --text:#444;
  --grey-bg:#ebebeb;
  --line:#bdbdbd;
  --white:#fff;
}
*{margin:0;padding:0;box-sizing:border-box}
html,body{width:1200px;height:3609px;overflow:hidden}
body{position:relative;font-family:"Open Sans",Arial,sans-serif;color:var(--text);background:var(--white)}
.abs{position:absolute}
.serif{font-family:"Tinos","Times New Roman",serif}

/* hero */
.hero{left:0;top:0;width:1200px;height:730px;
  background:
    radial-gradient(ellipse 260px 200px at 520px 470px,rgba(90,35,15,.55),rgba(90,35,15,0) 100%),
    radial-gradient(ellipse 500px 160px at 300px 190px,rgba(240,190,110,.45),rgba(240,190,110,0) 100%),
    linear-gradient(180deg,#a79a83 0%,#9a7a46 14%,#6a4a22 28%,#4f3c1c 40%,#6f7226 55%,#8f8a2e 75%,#6f6a24 100%)}
.navbar{left:0;top:49px;width:1200px;height:70px;background:var(--white)}
.nav{position:absolute;top:0;left:0;width:1200px;height:70px;list-style:none}
.nav li{position:absolute;top:25px;font-size:14.5px;color:#333;letter-spacing:.3px}
.nav li.active{color:var(--red);font-weight:600}
.nav-mark{left:489px;top:60px;width:42px;height:10px}
.brand{left:112px;top:0;width:206px;height:180px;background:var(--white);text-align:center;color:var(--red);font-family:"Tinos",serif}
.brand .b1{display:block;margin-top:50px;font-size:27px;letter-spacing:1px}
.brand .b2{display:block;margin-top:8px;font-size:18px;line-height:21px;letter-spacing:.5px}
.hero-title{left:0;top:244px;width:1200px;text-align:center;color:var(--white);font-size:31px;line-height:38px;font-weight:700;letter-spacing:.5px}
.hero-tag{left:0;top:328px;width:1200px;text-align:center;color:var(--white);font-size:28px}
.hero-note{left:0;top:373px;width:1200px;text-align:center;color:var(--white);font-size:16.5px}
.arrow{top:348px;width:20px;height:34px}
.hero-curve{left:0;top:650px;width:1200px;height:82px}

/* about */
.about-art{top:722px;height:126px;background:var(--red);border-radius:40px 40px 10px 10px}
.h2{left:0;width:1200px;text-align:center;color:var(--ink);font-family:"Tinos",serif;font-weight:700;font-size:34px;letter-spacing:.5px}
.lead{left:190px;width:820px;text-align:center;font-size:15.5px;line-height:25px;color:var(--text)}
.btn-outline{text-align:center;font-family:"Tinos",serif;font-size:21px;border:2px solid var(--red);color:var(--red);background:var(--white)}
.btn-fill{text-align:center;font-family:"Tinos",serif;font-size:21px;color:var(--white);background:var(--red)}

/* adopt */
.adopt{left:0;top:1199px;width:1200px;height:1030px;background:var(--grey-bg)}
.sub{left:0;width:1200px;text-align:center;font-size:15.5px;color:var(--text)}
.horse-card{width:311px;height:318px;background:var(--white);padding:4px;box-shadow:0 1px 4px rgba(0,0,0,.25)}
.horse-card div{width:100%;height:100%}

/* difference */
.difference{left:0;top:2229px;width:1200px;height:432px;
  background:
    radial-gradient(ellipse 300px 200px at 950px 330px,rgba(200,170,130,.55),rgba(200,170,130,0) 100%),
    radial-gradient(ellipse 320px 180px at 250px 380px,rgba(40,25,18,.6),rgba(40,25,18,0) 100%),
    linear-gradient(180deg,#6d6660 0%,#5e4a3a 35%,#4b3b2e 65%,#6a5642 100%)}
.difference-overlay{left:0;top:2229px;width:1200px;height:432px;background:rgba(30,20,15,.2)}

/* contact */
.info-icon{left:112px;width:41px;height:41px;border:2px solid var(--red);border-radius:50%;display:flex;align-items:center;justify-content:center}
.info-label{left:164px;font-family:"Tinos",serif;color:var(--red);font-size:15px}
.info-text{left:164px;font-size:11.5px;line-height:18px;color:#333}
.field{height:37px;border:1.5px solid var(--line);border-radius:3px;background:var(--white);font-size:12px;color:#777;padding:9px 16px;display:flex;align-items:center;gap:6px}
.field.area{align-items:flex-start;height:80px;padding-top:14px}
.captcha{left:430px;top:3090px;width:261px;height:63px;border:1.5px solid #d3d3d3;border-radius:3px;background:#f9f9f9}
.captcha .box{position:absolute;left:10px;top:20px;width:24px;height:24px;border:2px solid #c1c1c1;border-radius:2px;background:var(--white)}
.captcha .lbl{position:absolute;left:42px;top:22px;font-size:12px;color:#222}
.captcha .mark{position:absolute;left:218px;top:10px;width:24px;height:24px;background:#9bb3d8;border-radius:3px}
.captcha .fine{position:absolute;left:196px;top:38px;width:62px;font-size:7px;color:#777;text-align:center;line-height:9px}

/* footer */
.footer{left:0;top:3210px;width:1200px;height:399px;background:var(--red)}
.footer-cut{left:0;top:3209px;width:1200px;height:90px}
.f-brand{left:107px;top:3352px;width:130px;text-align:center;color:var(--white);font-family:"Tinos",serif}
.f-brand .b1{display:block;font-size:20px;letter-spacing:1px}
.f-brand .b2{display:block;font-size:13px;line-height:16px;margin-top:8px;letter-spacing:.3px}
.social{top:3473px;width:33px;height:33px;border-radius:50%;background:var(--white)}
.f-head{font-family:"Tinos",serif;color:var(--white);font-size:21px}
.f-links{list-style:none;font-size:12px;color:var(--white)}
.f-links li{height:25.8px}
.newsletter{left:805px;top:3390px;width:283px;height:47px;background:var(--white);font-size:12px;color:#333;padding:15px 16px}
.copy{left:0;top:3566px;width:1200px;text-align:center;color:var(--white);font-size:12px}
</style>
</head>
<body>

<!-- hero -->
<div class="abs hero" role="img" aria-label="Photo of a chestnut horse grazing in a golden sunlit pasture with a fence and barn behind"></div>
<div class="abs navbar">
  <ul class="nav">
    <li class="active" style="left:489px">HOME</li>
    <li style="left:579px">ABOUT</li>
    <li style="left:674px">ADOPT</li>
    <li style="left:768px">HORSES</li>
    <li style="left:870px">DONATE/SHOP</li>
    <li style="left:1021px">CONTACT</li>
  </ul>
</div>
<svg class="abs nav-mark" viewBox="0 0 42 10"><path d="M2 8 Q21 -2 40 3" stroke="#b00a22" stroke-width="2.5" fill="none" stroke-linecap="round"/></svg>
<div class="abs brand"><span class="b1">CORVALE</span><span class="b2">PADDOCK<br>REHOMING</span></div>

<h1 class="abs hero-title serif">WE SUPPORT AND DEVELOP RETIRED THOROUGHBRED<br>RACEHORSES FOR THEIR NEXT CHAPTER IN LIFE</h1>
<p class="abs hero-tag serif">Retire. Retrain. Rehome.</p>
<p class="abs hero-note">Corvale Paddock Rehoming Society (CPRS) is a registered not-for-profit organization in Corvale County.</p>
<svg class="abs arrow" style="left:42px" viewBox="0 0 20 34"><path d="M16 2 L4 17 L16 32" stroke="#fff" stroke-width="1.6" fill="none"/></svg>
<svg class="abs arrow" style="left:1126px" viewBox="0 0 20 34"><path d="M4 2 L16 17 L4 32" stroke="#fff" stroke-width="1.6" fill="none"/></svg>
<svg class="abs hero-curve" viewBox="0 0 1200 82" preserveAspectRatio="none">
  <path d="M0,76 Q600,-40 1200,76 L1200,82 L0,82Z" fill="#b00a22"/>
  <path d="M0,82 Q600,-10 1200,82Z" fill="#fff"/>
</svg>

<!-- about -->
<div class="abs about-art" style="left:418px;width:72px" role="img" aria-label="Silhouette illustration of a rider on a standing horse"></div>
<div class="abs about-art" style="left:552px;width:96px;top:732px;height:106px" role="img" aria-label="Silhouette illustration of a rider on a bucking horse"></div>
<div class="abs about-art" style="left:728px;width:66px" role="img" aria-label="Silhouette illustration of a rearing horse with rider"></div>

<h2 class="abs h2" style="top:868px">ABOUT US</h2>
<p class="abs lead" style="top:932px">The health, safety and welfare of our equine athletes does not end at the finish line, and retirement and aftercare are critical to the success of the racing industry.&nbsp; Aftercare is the safe placement of racehorses after their careers as racehorse are completed. Some horses might retire to the breeding shed or broodmare bands, while others are retrained for second careers.</p>
<div class="abs btn-outline" style="left:456px;top:1072px;width:288px;height:51px;line-height:47px">LEARN MORE ABOUT US</div>

<!-- adopt -->
<section class="abs adopt"></section>
<h2 class="abs h2" style="top:1252px">ADOPT A HORSE</h2>
<p class="abs sub" style="top:1306px">Corvale Paddock Rehoming is committed to helping match you with the perfect horse.</p>

<div class="abs horse-card" style="left:112px;top:1371px"><div role="img" aria-label="Photo of a dark bay horse head in a halter" style="background:radial-gradient(ellipse 110px 150px at 55% 55%,#2a2624,rgba(42,38,36,0) 100%),linear-gradient(180deg,#b7b2a4 0%,#9a978a 50%,#6d7a6c 100%)"></div></div>
<div class="abs horse-card" style="left:444px;top:1371px"><div role="img" aria-label="Photo of horses eating in a dusty corral beside stone stables" style="background:radial-gradient(ellipse 120px 40px at 45% 45%,rgba(40,30,25,.7),rgba(40,30,25,0) 100%),linear-gradient(180deg,#9fb1c6 0%,#b6b3a8 18%,#a78e6f 32%,#c7a77d 100%)"></div></div>
<div class="abs horse-card" style="left:777px;top:1371px"><div role="img" aria-label="Photo of horses grazing in a green field under a blue sky" style="background:radial-gradient(ellipse 90px 30px at 40% 25%,rgba(240,240,245,.8),rgba(240,240,245,0) 100%),linear-gradient(180deg,#2f5592 0%,#7f9dc7 55%,#2f4a1c 62%,#5f8a3a 80%,#6f9846 100%)"></div></div>
<div class="abs horse-card" style="left:112px;top:1706px"><div role="img" aria-label="Photo of a black horse cantering across grass" style="background:radial-gradient(ellipse 70px 100px at 50% 50%,rgba(25,22,22,.85),rgba(25,22,22,0) 100%),linear-gradient(180deg,#4c6a32 0%,#6e8d45 45%,#88a255 100%)"></div></div>
<div class="abs horse-card" style="left:444px;top:1706px"><div role="img" aria-label="Photo of two chestnut horses among sagebrush" style="background:radial-gradient(ellipse 60px 100px at 22% 30%,rgba(140,60,30,.8),rgba(140,60,30,0) 100%),radial-gradient(ellipse 50px 70px at 85% 40%,rgba(110,40,25,.8),rgba(110,40,25,0) 100%),linear-gradient(180deg,#4d5a3c 0%,#7a7a5a 50%,#a8a98a 100%)"></div></div>
<div class="abs horse-card" style="left:777px;top:1706px"><div role="img" aria-label="Photo of a chestnut horse with a white blaze in a stable" style="background:radial-gradient(ellipse 140px 150px at 60% 55%,#8a4a2a,rgba(138,74,42,0) 100%),linear-gradient(135deg,#1e1714,#3a2a22 50%,#2a1e19)"></div></div>

<div class="abs btn-fill" style="left:508px;top:2087px;width:184px;height:52px;line-height:52px">ADOPT NOW</div>

<!-- make a difference -->
<section class="abs difference" role="img" aria-label="Photo of horses moving through a dusty ranch corral"></section>
<div class="abs difference-overlay"></div>
<h2 class="abs h2" style="top:2314px;color:#fff">MAKE A DIFFERENCE</h2>
<p class="abs lead" style="top:2370px;left:160px;width:880px;color:#fff">But I must explain to you how all this mistaken idea of denouncing pleasure and praising pain was born and I will give you a complete account of the system, and expound the actual teachings of the great explorer of the truth, the master-builder of human happiness. No one rejects, dislikes, or avoids pleasure itself, because it is pleasure, but because those who do not know how to pursue pleasure rationally encounter consequences that are extremely painful.</p>
<div class="abs btn-outline" style="left:457px;top:2511px;width:287px;height:50px;line-height:46px;background:transparent;border-color:#fff;color:#fff">MORE WAYS TO GIVE</div>

<!-- contact -->
<h2 class="abs h2" style="top:2733px;font-size:36px">HAVE A QUESTION OR NEED MORE INFORMATION?</h2>
<p class="abs sub" style="top:2797px">Give us a call or use the form below.</p>

<div class="abs info-icon" style="top:2880px"><svg width="16" height="18" viewBox="0 0 16 18"><path d="M8 1a5.5 5.5 0 0 0-5.5 5.5C2.5 11 8 17 8 17s5.5-6 5.5-10.5A5.5 5.5 0 0 0 8 1z" fill="#b00a22"/><circle cx="8" cy="6.5" r="2" fill="#fff"/></svg></div>
<div class="abs info-label" style="top:2882px">LOCATION</div>
<p class="abs info-text" style="top:2906px">Corvale Paddock Rehoming,<br>Corvale County, 4402-RR 19, PO Box<br>2208, T0K 4P1</p>

<div class="abs info-icon" style="top:2984px"><svg width="16" height="16" viewBox="0 0 16 16"><path d="M4 1.5l2.5 3-1.5 1.7c.8 1.7 2.1 3 3.8 3.8L10.5 8.5l3 2.5-1.4 2.7C7 13.5 2.5 9 2.3 3z" fill="#b00a22"/></svg></div>
<div class="abs info-label" style="top:2986px">CALL US</div>
<p class="abs info-text" style="top:3011px">555-214-7730</p>

<div class="abs info-icon" style="top:3071px"><svg width="16" height="13" viewBox="0 0 16 13"><rect x="1" y="1" width="14" height="11" rx="1" fill="none" stroke="#b00a22" stroke-width="1.6"/><path d="M1.5 2 L8 7.5 L14.5 2" fill="none" stroke="#b00a22" stroke-width="1.6"/></svg></div>
<div class="abs info-label" style="top:3072px">EMAIL US</div>
<p class="abs info-text" style="top:3096px">info@corvalepaddock.org</p>

<div class="abs field" style="left:430px;top:2871px;width:326px">&#9679; First Name</div>
<div class="abs field" style="left:764px;top:2871px;width:325px">&#9679; Last Name</div>
<div class="abs field" style="left:430px;top:2931px;width:326px">&#9990; Your Phone</div>
<div class="abs field" style="left:764px;top:2931px;width:325px">&#9993; Your Email</div>
<div class="abs field area" style="left:430px;top:2990px;width:659px">&#9679; How Can we help you?</div>

<div class="abs captcha">
  <div class="box"></div>
  <div class="lbl">I'm not a robot</div>
  <div class="mark"></div>
  <div class="fine">Verify<br>Privacy - Terms</div>
</div>
<div class="abs btn-fill" style="left:894px;top:3104px;width:194px;height:49px;line-height:49px">SUBMIT NOW</div>

<!-- footer -->
<footer class="abs footer"></footer>
<svg class="abs footer-cut" viewBox="0 0 1200 90" preserveAspectRatio="none">
  <path d="M0,0 H1200 V12 Q600,150 0,12Z" fill="#fff"/>
  <path d="M0,14 Q600,118 1200,14" stroke="#f1d3d8" stroke-width="8" fill="none"/>
</svg>
<div class="abs f-brand"><span class="b1">CORVALE</span><span class="b2">PADDOCK<br>REHOMING</span></div>
<div class="abs social" style="left:112px" role="img" aria-label="Social profile link"></div>
<div class="abs social" style="left:155px" role="img" aria-label="Social profile link"></div>
<div class="abs social" style="left:198px" role="img" aria-label="Social profile link"></div>

<div class="abs f-head" style="left:359px;top:3344px">Links</div>
<ul class="abs f-links" style="left:361px;top:3387px">
  <li>Home</li><li>About</li><li>Adopt</li><li>Horses</li><li>Donate/Shop</li>
</ul>
<ul class="abs f-links" style="left:558px;top:3387px">
  <li>Terms and Conditions</li><li>Privacy Policy</li><li>Contact</li>
</ul>
<div class="abs f-head" style="left:805px;top:3344px">Join Our Newsletter</div>
<div class="abs newsletter">Email Address</div>
<svg class="abs" style="left:1056px;top:3406px" width="18" height="14" viewBox="0 0 18 14"><rect x="0" y="0" width="18" height="14" rx="2" fill="#b00a22"/><path d="M1.5 2 L9 8 L16.5 2" fill="none" stroke="#fff" stroke-width="1.6"/></svg>
<p class="abs copy">Copyright © 2021 Corvale Paddock Rehoming. All rights reserved.</p>

</body>
</html>
```